8 1/2 x 8 1/2 Social Media Design Ad - Commercial Loan Originator

Wanted
Commercial Loan Originators

* No Licensing Required
* Lend Nationwide with few exceptions
* Competitive Compensation
* You find the Investors and we handle the rest!!!

PRODUCTS
* Debt Service Coverage Loans (DSCR)
* Fix & Flip Financing
* Ground Up Construction
* Bridge Loans
* Portfolio Loans
And many more.....

Call (800) 417-9265 x24 for more information

Brightmoor Lending Partners, Inc.
7200 Warbleton Avenue, Harlow Springs, MD 20987
NMLS #318640

```html
<!DOCTYPE html>
<html lang="en">
<head>
<meta charset="utf-8">
<title>Wanted: Commercial Loan Originators</title>
<link href="https://fonts.googleapis.com/css2?family=Anton&family=Fira+Sans+Condensed:wght@500;600&family=Oswald:wght@500;600&family=Arimo:ital,wght@0,400;0,600;1,400&display=swap" rel="stylesheet">
<style>
  :root {
    --blue-deep: #1b3f9e;
    --blue-mid: #2a5bd0;
    --blue-light: #4f86dc;
    --navy: #1e3a8f;
    --gold: #d6a138;
    --gold-light: #f6dfa6;
    --white: #ffffff;
    --ink: #1c1c1c;
    --paper: #f6f7f9;
  }
  * { margin: 0; padding: 0; box-sizing: border-box; }
  html, body { width: 1200px; height: 1200px; overflow: hidden; background: var(--paper); }
  .ad { position: relative; width: 1200px; height: 1200px; background: var(--paper); overflow: hidden; }
  .ad-art { position: absolute; inset: 0; width: 1200px; height: 1200px; }
  .headline {
    position: absolute; left: 56px; top: 54px;
    font-family: "Anton", sans-serif; font-size: 158px; line-height: 1; letter-spacing: 14px;
    background: linear-gradient(90deg, var(--gold) 0%, var(--gold) 18%, var(--gold-light) 42%, var(--gold-light) 55%, var(--gold) 80%);
    -webkit-background-clip: text; background-clip: text; color: transparent;
  }
  .subhead {
    position: absolute; left: 58px; top: 222px;
    font-family: "Oswald", sans-serif; font-weight: 600; font-size: 45px; line-height: 1;
    color: var(--white); letter-spacing: 0.3px;
    transform: scaleX(0.915); transform-origin: left center;
  }
  .perks { position: absolute; left: 60px; top: 298px; list-style: none; }
  .perks li {
    position: relative; padding-left: 49px; margin-bottom: 20px;
    font-family: "Fira Sans Condensed", sans-serif; font-weight: 600; font-size: 25px;
    line-height: 28px; color: var(--white); text-transform: uppercase; letter-spacing: 0.6px;
  }
  .perks li.closing { margin-top: 8px; }
  .perks svg { position: absolute; left: 0; top: 0; width: 32px; height: 32px; }
  .products { position: absolute; left: 47px; top: 828px; border-left: 3px solid var(--navy); height: 160px; width: 940px; }
  .products h2 {
    position: absolute; left: 13px; top: 0;
    font-family: "Oswald", sans-serif; font-weight: 600; font-size: 30px; letter-spacing: 4px;
    color: var(--navy); line-height: 1;
  }
  .product-list { position: absolute; top: 49px; list-style: none; }
  .product-list.first { left: 13px; }
  .product-list.second { left: 418px; padding-left: 40px; border-left: 2px dotted var(--navy); height: 96px; }
  .product-list li {
    position: relative; padding-left: 33px; height: 37.5px;
    font-family: "Arimo", sans-serif; font-size: 19.5px; color: var(--ink); line-height: 24px;
  }
  .product-list svg { position: absolute; left: 0; top: 2px; width: 21px; height: 21px; }
  .product-list .more { padding-left: 0; margin-left: -8px; font-style: italic; }
  .call-band {
    position: absolute; left: 0; top: 1009px; width: 810px; height: 100px;
    background: linear-gradient(90deg, var(--navy) 0%, var(--blue-mid) 65%, var(--blue-light) 100%);
    border-top-right-radius: 36px;
    display: flex; align-items: center;
  }
  .call-label { margin-left: 57px; font-family: "Oswald", sans-serif; font-weight: 600; font-size: 31px; color: var(--gold); }
  .call-number { margin-left: 18px; font-family: "Oswald", sans-serif; font-weight: 600; font-size: 52px; color: var(--white); letter-spacing: 0.3px; }
  .call-divider { margin-left: 34px; width: 2px; height: 86px; background: rgba(255,255,255,0.6); }
  .call-more { margin-left: 34px; font-family: "Arimo", sans-serif; font-size: 23px; line-height: 28px; color: var(--white); text-transform: uppercase; }
  .address { position: absolute; left: 48px; top: 1132px; display: flex; align-items: center; }
  .address svg { width: 44px; height: 48px; }
  .address-text { margin-left: 24px; font-family: "Arimo", sans-serif; font-size: 19.5px; line-height: 24px; color: var(--ink); }
  .address-text strong { font-weight: 600; }
  .brand { position: absolute; left: 850px; top: 1010px; width: 300px; display: flex; align-items: center; gap: 12px; }
  .brand-dot { flex: none; width: 34px; height: 34px; border-radius: 50%; background: var(--navy); }
  .brand-name { font-family: "Oswald", sans-serif; font-weight: 600; font-size: 30px; line-height: 34px; color: var(--navy); text-transform: uppercase; }
</style>
</head>
<body>
<main class="ad">
  <svg class="ad-art" viewBox="0 0 1200 1200">
    <defs>
      <linearGradient id="hero-blue" x1="0" y1="0" x2="1" y2="1">
        <stop offset="0" stop-color="#1f48b4"/>
        <stop offset="0.5" stop-color="#2f63d4"/>
        <stop offset="1" stop-color="#1c45ad"/>
      </linearGradient>
      <linearGradient id="suit-tones" x1="0" y1="0" x2="0" y2="1">
        <stop offset="0" stop-color="#6d5448"/>
        <stop offset="0.35" stop-color="#7c8592"/>
        <stop offset="1" stop-color="#4f5866"/>
      </linearGradient>
      <linearGradient id="band-gold" x1="0" y1="0" x2="1" y2="0">
        <stop offset="0" stop-color="#d3a03a"/>
        <stop offset="0.55" stop-color="#f3d793"/>
        <stop offset="1" stop-color="#d69f30"/>
      </linearGradient>
      <linearGradient id="meeting-tones" x1="0" y1="0" x2="1" y2="1">
        <stop offset="0" stop-color="#c9b7a4"/>
        <stop offset="1" stop-color="#5b4a40"/>
      </linearGradient>
      <linearGradient id="office-tones" x1="0" y1="0" x2="1" y2="1">
        <stop offset="0" stop-color="#8fb3d6"/>
        <stop offset="1" stop-color="#e4e7ec"/>
      </linearGradient>
      <clipPath id="hero-clip">
        <path d="M0 0 H1200 V595 C1170 700 1100 870 920 880 C800 885 700 820 632 785 L0 510 Z"/>
      </clipPath>
    </defs>
    <path class="hero-backdrop" role="img" aria-label="Blue-tinted photo of a modern two-storey house" d="M0 0 H1200 V595 C1170 700 1100 870 920 880 C800 885 700 820 632 785 L0 510 Z" fill="url(#hero-blue)"/>
    <g clip-path="url(#hero-clip)">
      <rect class="hero-portrait" role="img" aria-label="Photo of a smiling businessman in a grey suit with arms crossed" x="640" y="178" width="525" height="720" rx="200" fill="url(#suit-tones)"/>
    </g>
    <path class="gold-swoosh" d="M0 510 L632 785 C700 820 800 885 920 880 C1040 875 1110 830 1140 800 C1090 880 1010 915 920 918 C800 920 700 850 632 805 L0 570 Z" fill="url(#band-gold)"/>
    <circle cx="300" cy="641" r="121" fill="#ffffff"/>
    <circle class="photo-meeting" role="img" aria-label="Photo of a loan officer meeting with clients at a table" cx="300" cy="641" r="115" fill="url(#meeting-tones)"/>
    <circle cx="513" cy="725" r="121" fill="#ffffff"/>
    <circle class="photo-office" role="img" aria-label="Photo of a young professional reviewing a tablet in an office" cx="513" cy="725" r="115" fill="url(#office-tones)"/>
  </svg>

  <h1 class="headline">WANTED</h1>
  <p class="subhead">COMMERCIAL LOAN ORIGINATORS</p>

  <ul class="perks">
    <li><svg viewBox="0 0 32 32"><circle cx="16" cy="16" r="14.5" fill="none" stroke="#d6a138" stroke-width="2"/><path d="M10 16.5 l4 4 l8 -9" fill="none" stroke="#d6a138" stroke-width="2"/></svg>No licensing required</li>
    <li><svg viewBox="0 0 32 32"><circle cx="16" cy="16" r="14.5" fill="none" stroke="#d6a138" stroke-width="2"/><path d="M10 16.5 l4 4 l8 -9" fill="none" stroke="#d6a138" stroke-width="2"/></svg>Lend nationwide with few exceptions</li>
    <li><svg viewBox="0 0 32 32"><circle cx="16" cy="16" r="14.5" fill="none" stroke="#d6a138" stroke-width="2"/><path d="M10 16.5 l4 4 l8 -9" fill="none" stroke="#d6a138" stroke-width="2"/></svg>Competitive compensation</li>
    <li class="closing"><svg viewBox="0 0 32 32"><circle cx="16" cy="16" r="14.5" fill="none" stroke="#d6a138" stroke-width="2"/><path d="M10 16.5 l4 4 l8 -9" fill="none" stroke="#d6a138" stroke-width="2"/></svg>You find the investors and<br>we handle the rest!!!</li>
  </ul>

  <section class="products">
    <h2>PRODUCTS</h2>
    <ul class="product-list first">
      <li><svg viewBox="0 0 22 22"><circle cx="11" cy="11" r="10" fill="none" stroke="#d6a138" stroke-width="1.5"/><path d="M6.5 11.5 l3 3 l6 -6.5" fill="none" stroke="#d6a138" stroke-width="1.5"/></svg>Debt Service Coverage Loans (DSCR)</li>
      <li><svg viewBox="0 0 22 22"><circle cx="11" cy="11" r="10" fill="none" stroke="#d6a138" stroke-width="1.5"/><path d="M6.5 11.5 l3 3 l6 -6.5" fill="none" stroke="#d6a138" stroke-width="1.5"/></svg>Fix &amp; Flip Financing</li>
      <li><svg viewBox="0 0 22 22"><circle cx="11" cy="11" r="10" fill="none" stroke="#d6a138" stroke-width="1.5"/><path d="M6.5 11.5 l3 3 l6 -6.5" fill="none" stroke="#d6a138" stroke-width="1.5"/></svg>Ground Up Construction</li>
    </ul>
    <ul class="product-list second">
      <li><svg viewBox="0 0 22 22"><circle cx="11" cy="11" r="10" fill="none" stroke="#d6a138" stroke-width="1.5"/><path d="M6.5 11.5 l3 3 l6 -6.5" fill="none" stroke="#d6a138" stroke-width="1.5"/></svg>Bridge Loans</li>
      <li><svg viewBox="0 0 22 22"><circle cx="11" cy="11" r="10" fill="none" stroke="#d6a138" stroke-width="1.5"/><path d="M6.5 11.5 l3 3 l6 -6.5" fill="none" stroke="#d6a138" stroke-width="1.5"/></svg>Portfolio Loans</li>
      <li class="more">And many more.....</li>
    </ul>
  </section>

  <div class="call-band">
    <span class="call-label">CALL</span>
    <span class="call-number">(800) 417-9265 X24</span>
    <span class="call-divider"></span>
    <span class="call-more">For more<br>information</span>
  </div>

  <div class="address">
    <svg viewBox="0 0 44 48"><path d="M22 4 a11 11 0 0 1 11 11 c0 8 -11 18 -11 18 s-11 -10 -11 -18 a11 11 0 0 1 11 -11 z" fill="none" stroke="#d6a138" stroke-width="2"/><circle cx="22" cy="15" r="4" fill="none" stroke="#d6a138" stroke-width="2"/><path d="M13 30 L2 37 L22 46 L42 37 L31 30" fill="none" stroke="#d6a138" stroke-width="2"/></svg>
    <p class="address-text"><strong>Brightmoor Lending Partners, Inc.</strong><br>7200 Warbleton Avenue, Harlow Springs, MD 20987 | NMLS #318640</p>
  </div>

  <div class="brand">
    <span class="brand-dot"></span>
    <span class="brand-name">Brightmoor Lending Partners</span>
  </div>
</main>
</body>
</html>
```